I need a book cover (front and back) for a book I wrote called "7 Habits of Polish: A Closet Method for Confidence".

The short version of the book can be found online here: https://filevault-share.example/file/d/8KpQm3RtZx2LwYv9NcHj4BsDf7GaUoEi/view

I'm working on expanding this into a real book (100+ pages, with images), and putting it on Brindlemart.

I'm the author, Lou Markovitch. I was named "Sharpest Gent of the Nation" by Dapperline Journal, and I would like to add that to the cover for credibility.

My website "About Page" has more info about me and my business Threadwork House: https://threadworkhouse.example/pages/about-us

I also attached the first version of the cover I made using Canva.

I have LOTS of images, if you need some (mannequins, models, garments, etc). See our website's blog for more ideas of the images we have: https://threadworkhouse.example/blogs/news

```html
<!DOCTYPE html>
<html lang="en">
<head>
<meta charset="utf-8">
<title>7 Habits of Polish – Cover</title>
<link rel="stylesheet" href="https://fonts.googleapis.com/css2?family=League+Gothic&family=Great+Vibes&family=Barlow+Condensed:ital,wght@0,600;1,600&family=Jost:wght@300;400&family=Carlito:ital,wght@0,400;0,700;1,400;1,700&display=swap">
<style>
  :root {
    --page: #ffffff;
    --back-paper: #e8e7e5;
    --ink: #2b2b2b;
    --ink-soft: #3c3c3c;
    --gold: #e2bd82;
    --white: #f5f3ef;
    --tweed: #5b2a1c;
    --tweed-dark: #2e1610;
    --navy: #1d2a4b;
    --portrait-bg: #a3a3a3;
  }
  * { box-sizing: border-box; margin: 0; padding: 0; }
  html, body { width: 1200px; height: 533px; overflow: hidden; background: var(--page); }
  .canvas { position: relative; width: 1200px; height: 533px; }

  /* ---------- front cover component (em-based, scales with font-size) ---------- */
  .front-cover {
    position: absolute;
    width: 34.5em;
    height: 51.8em;
    overflow: hidden;
    color: var(--white);
  }
  .front-cover .cover-photo {
    position: absolute; inset: 0;
    background:
      radial-gradient(ellipse 38% 70% at 50% 72%, var(--navy) 0%, var(--navy) 45%, rgba(29,42,75,0) 100%),
      radial-gradient(ellipse at 50% 40%, var(--tweed) 0%, var(--tweed-dark) 100%);
  }
  .front-cover .subtitle {
    position: absolute; top: 2.4em; left: 0; right: 0;
    text-align: center;
    font-family: "Barlow Condensed", sans-serif; font-weight: 600;
    font-size: 1.85em; letter-spacing: .11em;
    white-space: nowrap;
  }
  .front-cover .title-line {
    position: absolute; left: 1.5em; right: 0;
    text-align: center;
    font-family: "League Gothic", sans-serif;
    color: var(--gold);
    line-height: .75;
    transform: scaleY(1.55); transform-origin: top center;
    white-space: nowrap;
  }
  .front-cover .line-number { top: 2.36em; font-size: 5.8em; }
  .front-cover .line-habits { top: 3.6em; font-size: 5.8em; }
  .front-cover .line-polish { top: 4.67em; font-size: 6.6em; }
  .front-cover .title-script {
    position: absolute; left: 1.55em; top: 2.9em;
    font-family: "Great Vibes", cursive;
    font-size: 8em; line-height: 1;
    color: var(--gold);
  }
  .front-cover .author {
    position: absolute; top: 24.1em; left: 0; right: 0;
    text-align: center;
    font-family: "Jost", sans-serif; font-weight: 300;
    font-size: 1.85em; letter-spacing: .12em;
    white-space: nowrap;
  }
  .front-cover .accolade {
    position: absolute; top: 41.2em; left: 0; right: 0;
    text-align: center;
    font-family: "Barlow Condensed", sans-serif; font-weight: 600; font-style: italic;
    font-size: 1.15em;
    white-space: nowrap;
  }

  .cover-large { left: 173px; top: 82px; font-size: 7.1px; }
  .cover-small { left: 64px; top: 288px; font-size: 3.36px; }
  .cover-front { left: 854px; top: 9px; font-size: 10.03px; }

  /* ---------- back cover ---------- */
  .back-cover {
    position: absolute; left: 507px; top: 9px;
    width: 347px; height: 519px;
    background: var(--back-paper);
    color: var(--ink);
  }
  .back-title {
    position: absolute; top: 46px; left: 0; right: 0;
    text-align: center;
    font-family: "League Gothic", sans-serif; font-weight: 400;
    font-size: 24px; line-height: .75;
    transform: scaleY(1.5); transform-origin: top center;
    color: var(--ink);
    white-space: nowrap;
  }
  .back-title .script { font-family: "Great Vibes", cursive; font-size: 16px; margin: 0 2px; }
  .back-subtitle {
    position: absolute; top: 87px; left: 0; right: 0;
    text-align: center;
    font-family: "Barlow Condensed", sans-serif; font-weight: 600;
    font-size: 11.5px; letter-spacing: 1.6px;
    white-space: nowrap;
  }
  .author-portrait {
    position: absolute; left: 30px; top: 104px; width: 122px; height: 199px;
    background: radial-gradient(ellipse 45% 70% at 50% 65%, #34466e 0%, #34466e 40%, var(--portrait-bg) 100%);
  }
  .body-copy {
    font-family: "Carlito", sans-serif;
    font-size: 5.4px; line-height: 8.85px;
    color: var(--ink-soft);
  }
  .body-copy p + p { margin-top: 8.85px; }
  .bio-column { position: absolute; left: 159px; top: 106px; width: 156px; }
  .bio-column .lead { font-weight: 700; color: var(--ink); }
  .bio-wide { position: absolute; left: 30px; top: 316px; width: 288px; line-height: 8.4px; }
  .testimonial-heading {
    position: absolute; top: 374px; left: 30px; width: 288px;
    display: flex; align-items: center; gap: 14px;
    font-family: "Jost", sans-serif; font-weight: 400;
    font-size: 10px; letter-spacing: 2.6px;
    color: var(--ink);
  }
  .testimonial-heading::before, .testimonial-heading::after {
    content: ""; flex: 1; height: 1px; background: var(--ink);
  }
  .testimonials { position: absolute; left: 30px; top: 387px; width: 288px; line-height: 8px; }
  .testimonials p { font-style: italic; }
  .testimonials p + p { margin-top: 8px; }
  .testimonials .who { font-style: normal; font-weight: 700; color: var(--ink); }
</style>
</head>
<body>
<main class="canvas">

  <section class="front-cover cover-large" aria-label="Front cover">
    <div class="cover-photo" role="img" aria-label="Close-up photo of a rust tweed jacket lapel over a navy shirt"></div>
    <p class="subtitle">A CLOSET METHOD FOR CONFIDENCE</p>
    <p class="title-line line-number">7</p>
    <p class="title-line line-habits">HABITS</p>
    <p class="title-script">of</p>
    <p class="title-line line-polish">POLISH</p>
    <p class="author">LOU MARKOVITCH</p>
    <p class="accolade">"SHARPEST GENT OF THE NATION" BY DAPPERLINE JOURNAL</p>
  </section>

  <section class="front-cover cover-small" aria-label="Front cover, small">
    <div class="cover-photo" role="img" aria-label="Close-up photo of a rust tweed jacket lapel over a navy shirt"></div>
    <p class="subtitle">A CLOSET METHOD FOR CONFIDENCE</p>
    <p class="title-line line-number">7</p>
    <p class="title-line line-habits">HABITS</p>
    <p class="title-script">of</p>
    <p class="title-line line-polish">POLISH</p>
    <p class="author">LOU MARKOVITCH</p>
    <p class="accolade">"SHARPEST GENT OF THE NATION" BY DAPPERLINE JOURNAL</p>
  </section>

  <section class="back-cover" aria-label="Back cover">
    <h2 class="back-title">7 HABITS <span class="script">of</span> POLISH</h2>
    <p class="back-subtitle">A CLOSET METHOD FOR CONFIDENCE</p>
    <div class="author-portrait" role="img" aria-label="Portrait of the author standing in a navy three-piece suit"></div>

    <div class="body-copy bio-column">
      <p class="lead">I'm Lou Markovitch, founder and CEO.</p>
      <p>In 2009 I was named <em>"Sharpest Gent of the Nation"</em> by Dapperline Journal and for the next 10 years I apprenticed with the premier bespoke tailor in New York City; fitting customers of all shapes and sizes and designing their wardrobes from top to bottom.</p>
      <p>People traveled from all over the world to get fitted by me in New York. That's when I realized that most people don't have access to a knowledgeable stylist or a reliable tailor.</p>
      <p>This is why I created Threadwork House.</p>
      <p>Threadwork House is a full-service bespoke tailor shop that specializes in online bespoke fittings and personal custom wardrobes.</p>
      <p>We've worked with everybody from CEOs, political leaders, professional athletes and famous movie stars. We have customers in 30+ countries around the world and we've been featured in Tailor Quarterly, Dapperline Journal, The Metro Ledger, The Market Herald, The Morning Hour and hundreds of other publications.</p>
    </div>

    <div class="body-copy bio-wide">
      <p>I've personally seen the life-changing effect that a proper fitting and a well-styled wardrobe can have. I've helped people get raises and promotions, meet their future wives, become the leader of their social circles and significantly improve their overall confidence to live their best lives.</p>
      <p>In my book 7 Habits of Polish (which you can download for free here), I break-down my best tips from the past 15 years to help you dress with style and build a great wardrobe.</p>
    </div>

    <h3 class="testimonial-heading">TESTIMONIAL</h3>

    <div class="body-copy testimonials">
      <p>"TWH is an experience unlike any other. You have real experts (the best in the game) who work directly with you to pick the right clothes and make sure it all fits perfectly." -<span class="who">Marcus, Oregon</span></p>
      <p>"Working with Lou and TWH has truly been a life-changing experience. I can't recommend it enough. I went from no style to best-dressed at my company." -<span class="who">Dwight, Nevada</span></p>
      <p>"After working with TWH I'm a whole new person. I'm so confident and put together... I don't even recognize the old me." -<span class="who">Tomas, Arizona</span></p>
    </div>
  </section>

  <section class="front-cover cover-front" aria-label="Front cover, print">
    <div class="cover-photo" role="img" aria-label="Close-up photo of a rust tweed jacket lapel over a navy shirt"></div>
    <p class="subtitle">A CLOSET METHOD FOR CONFIDENCE</p>
    <p class="title-line line-number">7</p>
    <p class="title-line line-habits">HABITS</p>
    <p class="title-script">of</p>
    <p class="title-line line-polish">POLISH</p>
    <p class="author">LOU MARKOVITCH</p>
    <p class="accolade">"SHARPEST GENT OF THE NATION" BY DAPPERLINE JOURNAL</p>
  </section>

</main>
</body>
</html>
```